Looking for a modern website banner design

Bramblecrest Coaching Partners looking for the development of the main banner of the website. The project description and photos are included in the upload files.

```html
<!DOCTYPE html>
<html lang="en">
<head>
<meta charset="utf-8">
<title>Bramblecrest Coaching Partners – Athlete Testimonial Banner</title>
<link href="https://fonts.googleapis.com/css2?family=Montserrat:ital,wght@0,400;0,500;0,800;1,400&display=swap" rel="stylesheet">
<style>
  :root {
    --navy: #172b7a;
    --navy-deep: #10236a;
    --navy-haze: #3a4f9e;
    --crimson: #761029;
    --gold: #f6c945;
    --gold-line: #c9a23f;
    --ice: #dff7f5;
    --white: #ffffff;
    --kit-red: #b0202d;
    --kit-black: #1e1e24;
  }
  * { margin: 0; padding: 0; box-sizing: border-box; }
  html, body { width: 1200px; height: 562px; overflow: hidden; background: var(--navy); }
  .hero-banner {
    position: relative;
    width: 1200px;
    height: 562px;
    overflow: hidden;
    font-family: "Montserrat", sans-serif;
    color: var(--white);
  }
  .hero-graphics { position: absolute; inset: 0; }
  .testimonial {
    position: absolute;
    left: 744px;
    top: 124px;
    width: 412px;
  }
  .testimonial__mark { display: block; width: 62px; height: 44px; margin-left: -17px; margin-bottom: 12px; }
  .testimonial__quote {
    font-size: 17.6px;
    font-weight: 400;
    line-height: 26.3px;
  }
  .testimonial__author {
    margin-top: 16px;
    font-size: 15px;
    font-weight: 800;
    color: var(--gold);
  }
  .testimonial__team {
    font-size: 15px;
    font-style: italic;
    font-weight: 400;
    line-height: 22px;
    margin-top: 2px;
  }
</style>
</head>
<body>
<main class="hero-banner">
  <svg class="hero-graphics" width="1200" height="562" viewBox="0 0 1200 562" xmlns="http://www.w3.org/2000/svg">
    <defs>
      <linearGradient id="arenaTone" x1="0" y1="0" x2="1" y2="1">
        <stop offset="0" stop-color="#1d3285"/>
        <stop offset="0.6" stop-color="#1a2f80"/>
        <stop offset="1" stop-color="#13286f"/>
      </linearGradient>
      <linearGradient id="hazeTone" x1="0" y1="0" x2="1" y2="0">
        <stop offset="0" stop-color="var(--navy-haze)" stop-opacity="0"/>
        <stop offset="0.3" stop-color="var(--navy-haze)" stop-opacity="0.55"/>
        <stop offset="0.7" stop-color="var(--navy-haze)" stop-opacity="0.5"/>
        <stop offset="1" stop-color="var(--navy-haze)" stop-opacity="0"/>
      </linearGradient>
      <linearGradient id="playerTone" x1="0" y1="0" x2="0" y2="1">
        <stop offset="0" stop-color="var(--kit-red)"/>
        <stop offset="0.5" stop-color="#5a1420"/>
        <stop offset="1" stop-color="var(--kit-black)"/>
      </linearGradient>
    </defs>

    <rect class="arena-backdrop" width="1200" height="562" fill="url(#arenaTone)" role="img" aria-label="Blue-toned photo of an empty ice hockey arena with seating and rink boards"/>

    <rect class="faded-celebration-photo" x="70" y="0" width="680" height="562" fill="url(#hazeTone)" role="img" aria-label="Faded blue-tinted close-up photo of the player smiling and celebrating"/>

    <polygon class="accent-band" points="0,0 72,0 740,562 475,562 0,153" fill="var(--crimson)" opacity="0.9"/>

    <line class="accent-rule" x1="34" y1="200" x2="656" y2="474" stroke="var(--gold-line)" stroke-width="2.2"/>

    <rect class="athlete-photo" x="228" y="78" width="322" height="484" fill="url(#playerTone)" role="img" aria-label="Cut-out photo of the hockey player in a red and black jersey, arms raised in celebration holding his stick"/>

    <line class="accent-stripe" x1="0" y1="183" x2="72" y2="243" stroke="var(--ice)" stroke-width="8"/>
    <line class="accent-stripe" x1="620" y1="431" x2="737" y2="516" stroke="var(--ice)" stroke-width="8"/>

    <text class="athlete-name-outline" x="27" y="487" font-family="Montserrat, sans-serif" font-weight="500" font-size="176" textLength="642" lengthAdjust="spacingAndGlyphs" fill="none" stroke="var(--white)" stroke-width="1">MARCUS</text>
  </svg>

  <section class="testimonial">
    <svg class="testimonial__mark" viewBox="0 0 62 44" aria-hidden="true">
      <circle cx="15" cy="30" r="14" fill="var(--gold)"/>
      <path d="M2 27 C4 13 12 4 25 0 L27 5 C19 9 15 15 14 20 Z" fill="var(--gold)"/>
      <circle cx="47" cy="30" r="14" fill="var(--gold)"/>
      <path d="M34 27 C36 13 44 4 57 0 L59 5 C51 9 47 15 46 20 Z" fill="var(--gold)"/>
    </svg>
    <p class="testimonial__quote">Bramblecrest has provided support that has allowed me to develop as a person and an athlete. The P.A.C.E.™ process allowed me to stay focused on attainable goals each season and progress from Junior to College and now Professional Hockey.</p>
    <p class="testimonial__author">Marcus Delaney</p>
    <p class="testimonial__team">Riverton Rapids<br>Eastern Seaboard Hockey League</p>
  </section>
</main>
</body>
</html>
```